Webdesign für Projektmanagement
Zielgruppe
Projektmanagement und Projektsteuerung von Bauvorhaben für Projektentwickler und Bauträger.
Wesentliche Bereiche sind Wirtschaftliche Steuerung, Steuerung der Baustelle und Bauabläufe sowie Steuerung der Marketing und Vertriebsaktivitäten.
Aufgabenstellung
Orientierung am Logo. Logo und Visitenkarte liegen bei. Schriftart Prelo und Prelo Slab.

```html
<!DOCTYPE html>
<html lang="de">
<head>
<meta charset="utf-8">
<title>Velhaus Real Estate – Webdesign</title>
<link href="https://fonts.googleapis.com/css2?family=Raleway:ital,wght@0,300;0,400;0,500;0,600;0,700;1,400&display=swap" rel="stylesheet">
<style>
:root{
  --stage:#04172a;
  --navy:#0f2b48;
  --gold:#a8955a;
  --gold-text:#a38f4e;
  --hero-a:#bfae72;
  --hero-b:#a8965a;
  --panel:#f5f3ef;
  --line:#ecebe7;
  --white:#ffffff;
  --body:#3d4652;
}
*{margin:0;padding:0;box-sizing:border-box}
html,body{width:1004px;height:1200px;overflow:hidden}
body{background:var(--stage);font-family:'Raleway',sans-serif;color:var(--body);position:relative}
.screen{position:absolute;left:53px;width:899px;height:518px;overflow:hidden;background:var(--hero-b)}
.screen--about{top:53px}
.screen--projects{top:608px}
.sidebar{position:absolute;left:0;top:0;width:138px;height:100%;background:var(--white)}
.brand{position:absolute;left:21px;top:55px;display:flex;align-items:center;gap:7px}
.brand__mark{width:9px;height:9px;background:var(--navy);flex:none}
.brand__name{font-family:'Raleway',sans-serif;font-weight:600;font-size:15px;color:var(--navy);letter-spacing:.6px;line-height:1}
.nav{position:absolute;left:0;top:127px;width:138px;list-style:none;border-top:1px solid var(--line)}
.nav li{height:27.5px;border-bottom:1px solid var(--line);display:flex;align-items:center;justify-content:space-between;padding:0 14px 0 21px;font-size:7.6px;font-weight:500;letter-spacing:.5px;color:var(--navy)}
.nav li.is-active{color:var(--gold-text);font-weight:700}
.nav .search{font-style:italic;color:#8a8f98;font-weight:400;letter-spacing:0;justify-content:flex-start;gap:7px}
.social{position:absolute;left:30px;top:492px;display:flex;gap:9px}
.social span{width:9px;height:9px;border-radius:50%;background:var(--navy)}
.main{position:absolute;left:138px;top:0;right:0;bottom:0}
.hero-bg{position:absolute;inset:0}
.hero-bg--office{background:linear-gradient(135deg,#c6b67b 0%,#b8a86c 45%,#a89659 100%)}
.hero-bg--plans{background:linear-gradient(160deg,#bcac70 0%,#ad9c60 60%,#9f8d51 100%)}
.topbar{position:absolute;left:0;top:0;right:0;height:26px;background:rgba(255,255,255,.12);display:flex;align-items:center;padding-left:47px;gap:16px;font-size:7.3px;color:var(--white)}
.topbar__item{display:flex;align-items:center;gap:4px}
.topbar svg{flex:none}
.kicker{position:absolute;left:47px;top:119px;font-size:13.5px;font-weight:700;color:var(--navy);letter-spacing:.4px}
.title{position:absolute;left:46px;top:140px;font-size:45px;font-weight:300;color:var(--white);letter-spacing:1px;line-height:1.1}
.intro{position:absolute;left:47px;top:222px;width:325px;height:320px;background:var(--panel);padding:22px 15px 0 15px}
.intro h2{font-size:12.4px;font-weight:600;color:var(--navy);letter-spacing:.8px;line-height:1.55;margin-bottom:9px}
.intro p{font-size:8.5px;line-height:12.8px;margin-bottom:7px}
.person{position:absolute;left:388px;width:325px;height:126px;background:var(--panel);display:flex}
.person--first{top:222px}
.person--second{top:360px}
.person__photo{width:139px;height:100%;flex:none}
.person__photo--first{background:linear-gradient(160deg,#1a1a1a 0%,#5a5a5a 55%,#2a2a2a 100%)}
.person__photo--second{background:linear-gradient(120deg,#e6e6e6 0%,#9a9a9a 45%,#3c3c3c 100%)}
.person__info{padding:19px 12px 0 12px}
.person__name{font-size:9.6px;font-weight:600;color:var(--navy);letter-spacing:.7px}
.person__role{font-size:8.4px;font-style:italic;margin-top:2px;margin-bottom:12px}
.person__contact{font-size:8.4px;line-height:12.8px}
.project{position:absolute;left:47px;width:666px;height:190px;background:var(--panel);display:flex}
.project--first{top:222px}
.project--second{top:428px}
.project__text{width:341px;padding:14px 15px 0 15px}
.project__category{font-size:7.8px;font-style:italic;color:#6b7079}
.project__name{font-size:13px;font-weight:700;color:var(--navy);letter-spacing:1px;margin:2px 0 7px}
.project__desc{font-size:8.5px;line-height:12.8px;margin-bottom:9px}
.checklist{list-style:none}
.checklist li{display:flex;align-items:center;gap:7px;font-size:8.5px;height:20.5px}
.project__image{width:325px;height:100%;flex:none}
.project__image--tower{background:linear-gradient(180deg,#c9dbe9 0%,#a9a7a3 35%,#6e6a66 75%,#9aa36a 100%)}
.project__image--estate{background:linear-gradient(180deg,#bcd6ea 0%,#e0e8ee 35%,#5e7f3e 70%,#3d5f28 100%)}
</style>
</head>
<body>

<section class="screen screen--about">
  <aside class="sidebar">
    <div class="brand"><span class="brand__mark"></span><span class="brand__name">Velhaus</span></div>
    <ul class="nav">
      <li>HOME</li>
      <li>LEISTUNGEN</li>
      <li class="is-active">ÜBER UNS <svg width="5" height="7" viewBox="0 0 5 7"><path d="M1 1l2.5 2.5L1 6" fill="none" stroke="#a38f4e" stroke-width=".8"/></svg></li>
      <li>PROJEKTE <svg width="5" height="7" viewBox="0 0 5 7"><path d="M1 1l2.5 2.5L1 6" fill="none" stroke="#a38f4e" stroke-width=".8"/></svg></li>
      <li>PARTNER</li>
      <li>KONTAKT</li>
      <li class="search"><svg width="6" height="6" viewBox="0 0 6 6"><circle cx="2.5" cy="2.5" r="1.7" fill="none" stroke="#a38f4e" stroke-width=".9"/><path d="M3.8 3.8L5.5 5.5" stroke="#a38f4e" stroke-width=".9"/></svg>Suchen</li>
    </ul>
    <div class="social"><span></span><span></span><span></span><span></span></div>
  </aside>
  <div class="main">
    <div class="hero-bg hero-bg--office" role="img" aria-label="Gedämpftes Foto eines Büros mit Bauplänen in Goldton"></div>
    <div class="topbar">
      <span class="topbar__item"><svg width="6" height="9" viewBox="0 0 6 9"><path d="M1.5 .5l1.3 2-1 .8c.3 1.4 1 2.5 2 3.2l1-.6 1 1.8-1.3.8C2.2 7.9.4 5 .6 1.2z" fill="#0f2b48"/></svg>+49 (0)211 - 555 019 20</span>
      <span class="topbar__item"><svg width="9" height="9" viewBox="0 0 9 9"><circle cx="4.5" cy="4.5" r="3.8" fill="none" stroke="#0f2b48" stroke-width=".9"/><path d="M4.5 2.2v2.5h1.8" fill="none" stroke="#0f2b48" stroke-width=".9"/></svg>Mo - Fr 9:00 - 18:00</span>
      <span class="topbar__item"><svg width="9" height="7" viewBox="0 0 9 7"><rect x=".5" y=".5" width="8" height="6" fill="none" stroke="#0f2b48" stroke-width=".9"/><path d="M.5 .5l4 3.3 4-3.3" fill="none" stroke="#0f2b48" stroke-width=".9"/></svg>info@velhaus.de</span>
      <span class="topbar__item"><svg width="7" height="9" viewBox="0 0 7 9"><path d="M3.5 .5A3 3 0 0 1 6.5 3.5C6.5 5.5 3.5 8.7 3.5 8.7S.5 5.5.5 3.5a3 3 0 0 1 3-3z" fill="#0f2b48"/><circle cx="3.5" cy="3.4" r="1.1" fill="#c6b67b"/></svg>Lindenallee 14, 40210 Düsseldorf</span>
    </div>
    <div class="kicker">VELHAUS REAL ESTATE</div>
    <h1 class="title">ÜBER UNS</h1>
    <article class="intro">
      <h2>PROJEKTMANAGEMENT UND<br>PROJEKTSTEUERUNG VON BAUVORHABEN</h2>
      <p>Die zunehmende Urbanisierung hat den Immobilienmarkt in den letzten Jahren nachhaltig verändert. Als Teil des größten Ballungszentrums Europas, hat dies starke Auswirkungen auf die Metropolregion Köln, Düsseldorf und Bonn. Begleitet wird diese Entwicklung durch vielschichtige städtebauliche Maßnahmen in der Region.</p>
      <p>Die Konsequenz aus dieser Entwicklung ist ein hoher Investitions-, Umnutzungs- und Projektentwicklungsbedarf bei Immobilien. Daraus entstanden ist ein für Investoren strukturell attraktiver Markt.</p>
      <p>In diesem Umfeld bietet die Velhaus Real Estate GmbH ihren Kunden maßgeschneiderte Dienstleistungen für Immobilienportfolios an.</p>
      <p>Lorem ipsum dolor sit amet, consetetur sadipscing elitr, sed diam nonumy eirmod tempor invidunt ut labore et dolore magna aliquyam erat, sed diam voluptua. At vero eos et accusam et justo duo dolores et ea rebum. Stet clita kasd gubergren, no sea takimata sanctus est Lorem ipsum dolor sit amet. Lorem ipsum dolor sit amet, consetetur sadipscing elitr, sed diam nonumy eirmod tempor invidunt ut labore et dolore magna aliquyam erat,</p>
    </article>
    <div class="person person--first">
      <div class="person__photo person__photo--first" role="img" aria-label="Schwarzweißes Porträtfoto des Geschäftsführers"></div>
      <div class="person__info">
        <div class="person__name">JÖRG WENDELMAIER</div>
        <div class="person__role">Geschäftsführer</div>
        <div class="person__contact">E-Mail: jorg.wendelmaier@velhaus.de<br>Mobil: +49 170 555 01 42</div>
      </div>
    </div>
    <div class="person person--second">
      <div class="person__photo person__photo--second" role="img" aria-label="Schwarzweißes Porträtfoto des zweiten Geschäftsführers vor einer Treppe"></div>
      <div class="person__info">
        <div class="person__name">LUKAS BERENDT</div>
        <div class="person__role">Geschäftsführer</div>
        <div class="person__contact">E-Mail: lukas.berendt@velhaus.de<br>Mobil: +49 160 555 03 87</div>
      </div>
    </div>
  </div>
</section>

<section class="screen screen--projects">
  <aside class="sidebar">
    <div class="brand"><span class="brand__mark"></span><span class="brand__name">Velhaus</span></div>
    <ul class="nav">
      <li>HOME</li>
      <li>LEISTUNGEN</li>
      <li class="is-active">ÜBER UNS <svg width="5" height="7" viewBox="0 0 5 7"><path d="M1 1l2.5 2.5L1 6" fill="none" stroke="#a38f4e" stroke-width=".8"/></svg></li>
      <li>PROJEKTE <svg width="5" height="7" viewBox="0 0 5 7"><path d="M1 1l2.5 2.5L1 6" fill="none" stroke="#a38f4e" stroke-width=".8"/></svg></li>
      <li>PARTNER</li>
      <li>KONTAKT</li>
      <li class="search"><svg width="6" height="6" viewBox="0 0 6 6"><circle cx="2.5" cy="2.5" r="1.7" fill="none" stroke="#a38f4e" stroke-width=".9"/><path d="M3.8 3.8L5.5 5.5" stroke="#a38f4e" stroke-width=".9"/></svg>Suchen</li>
    </ul>
    <div class="social"><span></span><span></span><span></span><span></span></div>
  </aside>
  <div class="main">
    <div class="hero-bg hero-bg--plans" role="img" aria-label="Gedämpftes Foto von Bauplänen und einem Schutzhelm in Goldton"></div>
    <div class="topbar">
      <span class="topbar__item"><svg width="6" height="9" viewBox="0 0 6 9"><path d="M1.5 .5l1.3 2-1 .8c.3 1.4 1 2.5 2 3.2l1-.6 1 1.8-1.3.8C2.2 7.9.4 5 .6 1.2z" fill="#0f2b48"/></svg>+49 (0)211 - 555 019 20</span>
      <span class="topbar__item"><svg width="9" height="9" viewBox="0 0 9 9"><circle cx="4.5" cy="4.5" r="3.8" fill="none" stroke="#0f2b48" stroke-width=".9"/><path d="M4.5 2.2v2.5h1.8" fill="none" stroke="#0f2b48" stroke-width=".9"/></svg>Mo - Fr 9:00 - 18:00</span>
      <span class="topbar__item"><svg width="9" height="7" viewBox="0 0 9 7"><rect x=".5" y=".5" width="8" height="6" fill="none" stroke="#0f2b48" stroke-width=".9"/><path d="M.5 .5l4 3.3 4-3.3" fill="none" stroke="#0f2b48" stroke-width=".9"/></svg>info@velhaus.de</span>
      <span class="topbar__item"><svg width="7" height="9" viewBox="0 0 7 9"><path d="M3.5 .5A3 3 0 0 1 6.5 3.5C6.5 5.5 3.5 8.7 3.5 8.7S.5 5.5.5 3.5a3 3 0 0 1 3-3z" fill="#0f2b48"/><circle cx="3.5" cy="3.4" r="1.1" fill="#bcac70"/></svg>Lindenallee 14, 40210 Düsseldorf</span>
    </div>
    <div class="kicker">VELHAUS REAL ESTATE</div>
    <h1 class="title">PROJEKTE &amp; REFERENZEN</h1>
    <article class="project project--first">
      <div class="project__text">
        <div class="project__category">Immobilienmanagement</div>
        <h2 class="project__name">PROJEKTNAME</h2>
        <p class="project__desc">Begleitung einer Portfolioliquidierung eines luxemburgischen<br>institutionellen Investors</p>
        <ul class="checklist">
          <li><svg width="9" height="8" viewBox="0 0 9 8"><path d="M1 4.2l2.3 2.5L8 1" fill="none" stroke="#0f2b48" stroke-width="1.6"/></svg>Portfolio-Analyse</li>
          <li><svg width="9" height="8" viewBox="0 0 9 8"><path d="M1 4.2l2.3 2.5L8 1" fill="none" stroke="#0f2b48" stroke-width="1.6"/></svg>Begleitung der Immobilientransaktionen</li>
          <li><svg width="9" height="8" viewBox="0 0 9 8"><path d="M1 4.2l2.3 2.5L8 1" fill="none" stroke="#0f2b48" stroke-width="1.6"/></svg>Reporting</li>
        </ul>
      </div>
      <div class="project__image project__image--tower" role="img" aria-label="Foto eines modernen Wohnhauses mit Balkonen"></div>
    </article>
    <article class="project project--second">
      <div class="project__text">
        <div class="project__category">Immobiliensanierung</div>
        <h2 class="project__name">PROJEKTNAME</h2>
        <p class="project__desc">Begleitung einer Portfolioliquidierung eines luxemburgischen<br>institutionellen Investors</p>
        <ul class="checklist">
          <li><svg width="9" height="8" viewBox="0 0 9 8"><path d="M1 4.2l2.3 2.5L8 1" fill="none" stroke="#0f2b48" stroke-width="1.6"/></svg>Portfolio-Analyse</li>
        </ul>
      </div>
      <div class="project__image project__image--estate" role="img" aria-label="Foto eines sanierten Altbaus zwischen Bäumen"></div>
    </article>
  </div>
</section>

</body>
</html>
```